A new presentation to our clients

we are a Real Estate agency, our website is www.dorelumia.com and it’s time to have a new, fashion and remarcable Business Card. we want to differentiate ourselves from other companies so we want a business card that differentiates us. we want the business card to impact our customers. in the competitive market that we have today, we have to be different and it is this difference that we seek

Target Market(s)

Real Estate Clients

Contact Information for Business Card

We search a totaly diferent card from the usual

Font styles to use
Sans Serif

Colors
e34197

Requirements
Must have
• Logo, adress, phone contact, e-mail, photo, and our website
Nice to have
• We would like to see a modern business card
Should not have
• Houses or building draws

```html
<!DOCTYPE html>
<html lang="pt">
<head>
<meta charset="utf-8">
<title>Dore Lumia – Business Card</title>
<link href="https://fonts.googleapis.com/css2?family=Open+Sans:wght@400&family=Roboto:wght@500;700&display=swap" rel="stylesheet">
<style>
  :root {
    --backdrop: #5c5c5c;
    --brand-pink: #e3216e;
    --brand-pink-light: #e8307a;
    --card-white: #f3f3f3;
    --ink: #333333;
    --white: #ffffff;
  }
  * { margin: 0; padding: 0; box-sizing: border-box; }
  html, body {
    width: 1200px;
    height: 900px;
    overflow: hidden;
    background: var(--backdrop);
  }
  .canvas {
    position: relative;
    width: 1200px;
    height: 900px;
  }
  .card {
    position: absolute;
    top: 200px;
    width: 310px;
    height: 502px;
    overflow: hidden;
  }
  .card-front {
    left: 253px;
    background: var(--card-white);
    border-radius: 66px 0 66px 0;
  }
  .card-back {
    left: 627px;
    border-radius: 0 66px 0 66px;
    background: var(--brand-pink);
  }
  .back-pattern {
    position: absolute;
    inset: 0;
    background: linear-gradient(135deg, var(--brand-pink-light) 0%, var(--brand-pink) 55%, var(--brand-pink-light) 100%);
  }
  .wordmark {
    position: absolute;
    left: 0;
    right: 0;
    text-align: center;
    font-family: "Roboto", sans-serif;
    font-weight: 500;
    letter-spacing: 0.5px;
    line-height: 1;
  }
  .card-front .wordmark {
    top: 146px;
    font-size: 46px;
    color: var(--brand-pink);
  }
  .card-back .wordmark {
    top: 228px;
    font-size: 40px;
    color: var(--white);
  }
  .contact-block {
    position: absolute;
    left: 36px;
    top: 307px;
    font-family: "Open Sans", sans-serif;
    color: var(--ink);
  }
  .person-name {
    font-family: "Roboto", sans-serif;
    font-weight: 700;
    font-size: 17px;
    color: var(--brand-pink);
    line-height: 20px;
  }
  .person-role {
    font-size: 14px;
    line-height: 18px;
  }
  .contact-list {
    list-style: none;
    margin-top: 7px;
  }
  .contact-list li {
    display: flex;
    align-items: center;
    font-size: 14px;
    line-height: 18px;
  }
  .contact-list svg {
    width: 11px;
    height: 11px;
    margin-right: 5px;
    fill: var(--brand-pink);
    flex: none;
  }
  .address {
    margin-top: 5px;
    font-size: 14px;
    line-height: 18px;
  }
</style>
</head>
<body>
<main class="canvas">

  <section class="card card-front">
    <div class="wordmark">Dore Lumia</div>

    <div class="contact-block">
      <div class="person-name">MARCUS BELLAMY</div>
      <div class="person-role">Managing Director</div>

      <ul class="contact-list">
        <li>
          <svg viewBox="0 0 12 12" aria-hidden="true"><path d="M1 4c0-2 2-3 5-3s5 1 5 3v1H8.5V3.8h-5V5H1zM3 6h6l1.5 5h-9z"/></svg>
          (+351) 210 555 014
        </li>
        <li>
          <svg viewBox="0 0 12 12" aria-hidden="true"><path d="M3 0h6v3H3zM0 4h12v5h-2V7H2v2H0zM3 8h6v4H3z"/></svg>
          (+351) 210 555 019
        </li>
        <li>
          <svg viewBox="0 0 12 12" aria-hidden="true"><path d="M0 2h12v1L6 7 0 3zM0 4.5l6 4 6-4V10H0z"/></svg>
          geral@dorelumia.com
        </li>
        <li>
          <svg viewBox="0 0 12 12" aria-hidden="true"><circle cx="6" cy="6" r="5.5"/><path d="M3 4.5h2.5l1 2-1.5 2.5M7.5 2.5l1 2h2" stroke="#f3f3f3" stroke-width="1.1" fill="none"/></svg>
          www.dorelumia.com
        </li>
      </ul>

      <div class="address">
        Rua das Acácias, 118<br>
        4410-052, Vila Serena
      </div>
    </div>
  </section>

  <section class="card card-back">
    <div class="back-pattern" role="img" aria-label="Faint diagonal repeated brand-name pattern on pink"></div>
    <div class="wordmark">Dore Lumia</div>
  </section>

</main>
</body>
</html>
```